Financial Service Company Need Business Card Design

This is a new startup company, first of its kind to offer this service. We facilitate the movement of deposit funds electronically between home buyers and real estate brokerages.Our customers are DOMIVANS®, real estate brokerages, and home buyers, we identify ourselves as a financial/technology company.
Not looking for anything too flashy. Just a clean design that shows the logo, contact info, etc. Company colors can be seen on attached logo, and 'coming soon page'
www.quorvanta.ca

```html
<!DOCTYPE html>
<html lang="en">
<head>
<meta charset="utf-8">
<title>Quorvanta – Business Card</title>
<link rel="stylesheet" href="https://fonts.googleapis.com/css2?family=Open+Sans:wght@400;600;700&display=swap">
<style>
  :root {
    --page-bg: #ecebe8;
    --card-bg: #2b2b2d;
    --card-bg-deep: #222224;
    --band: #1d1d1f;
    --brand-grey: #b9b9bb;
    --brand-orange: #e2663a;
    --text-light: #e6e6e6;
    --text-muted: #c9c9cb;
    --accent-blue: #5bb9dc;
    --divider: #3a3a3d;
  }
  * { margin: 0; padding: 0; box-sizing: border-box; }
  html, body {
    width: 1200px;
    height: 800px;
    overflow: hidden;
    background: var(--page-bg);
    font-family: "Open Sans", Arial, sans-serif;
  }
  .canvas {
    position: relative;
    width: 1200px;
    height: 800px;
    display: flex;
    align-items: center;
    justify-content: center;
    gap: 60px;
  }
  .card {
    position: relative;
    width: 520px;
    height: 297px;
    border-radius: 4px;
    background: linear-gradient(160deg, var(--card-bg) 0%, var(--card-bg-deep) 100%);
    box-shadow: 0 10px 30px rgba(0, 0, 0, 0.25);
    overflow: hidden;
  }

  /* Front */
  .card-front .brand-band {
    position: absolute;
    left: 40px;
    right: 40px;
    top: 88px;
    height: 120px;
    background: radial-gradient(ellipse at center, var(--band) 0%, rgba(29, 29, 31, 0) 72%);
  }
  .card-front .brand {
    position: absolute;
    left: 70px;
    top: 110px;
  }
  .brand-lockup {
    display: flex;
    align-items: center;
    gap: 14px;
  }
  .brand-mark {
    width: 34px;
    height: 34px;
    background: var(--brand-orange);
  }
  .brand-name {
    font-weight: 700;
    font-size: 44px;
    line-height: 1;
    letter-spacing: -0.5px;
    color: var(--brand-grey);
  }
  .brand-url {
    margin-top: 12px;
    margin-left: 48px;
    font-weight: 700;
    font-size: 21px;
    letter-spacing: 0.3px;
    color: var(--brand-orange);
  }

  /* Back */
  .card-back .person {
    position: absolute;
    left: 40px;
    top: 52px;
  }
  .person-name {
    font-size: 19px;
    font-weight: 400;
    letter-spacing: 1.5px;
    color: var(--text-light);
  }
  .person-role {
    margin-top: 2px;
    font-size: 16px;
    letter-spacing: 2px;
    color: var(--accent-blue);
  }
  .card-back .divider {
    position: absolute;
    top: 0;
    bottom: 0;
    width: 1px;
    background: var(--divider);
  }
  .divider-left { left: 240px; }
  .divider-right { left: 300px; }
  .contact-list {
    position: absolute;
    left: 240px;
    right: 0;
    top: 58px;
    list-style: none;
  }
  .contact-item {
    display: flex;
    align-items: center;
    height: 62px;
  }
  .contact-icon {
    width: 60px;
    display: flex;
    justify-content: center;
  }
  .contact-icon svg { width: 22px; height: 22px; }
  .contact-text {
    padding-left: 26px;
    font-size: 15px;
    letter-spacing: 0.5px;
    color: var(--text-muted);
  }
  .contact-text.is-link { color: var(--accent-blue); }
</style>
</head>
<body>
<main class="canvas">

  <section class="card card-front" aria-label="Card front">
    <div class="brand-band"></div>
    <div class="brand">
      <div class="brand-lockup">
        <span class="brand-mark"></span>
        <span class="brand-name">Quorvanta</span>
      </div>
      <div class="brand-url">www.quorvanta.ca</div>
    </div>
  </section>

  <section class="card card-back" aria-label="Card back">
    <div class="person">
      <div class="person-name">NAME SURNAME</div>
      <div class="person-role">OCCUPATION</div>
    </div>
    <span class="divider divider-left"></span>
    <span class="divider divider-right"></span>
    <ul class="contact-list">
      <li class="contact-item">
        <span class="contact-icon">
          <svg viewBox="0 0 24 24" fill="none" stroke="#b9b9bb" stroke-width="1.6" stroke-linejoin="round" aria-hidden="true">
            <path d="M6.5 3.5l3 .5 1.2 4-2 1.5a11 11 0 0 0 5.8 5.8l1.5-2 4 1.2.5 3c-.2 1.3-1.2 2-2.5 2A16 16 0 0 1 4.5 6c0-1.3.7-2.3 2-2.5z"/>
          </svg>
        </span>
        <span class="contact-text">123 456 789</span>
      </li>
      <li class="contact-item">
        <span class="contact-icon">
          <svg viewBox="0 0 24 24" fill="none" stroke="#5bb9dc" stroke-width="1.6" aria-hidden="true">
            <circle cx="12" cy="12" r="9"/>
            <ellipse cx="12" cy="12" rx="4" ry="9"/>
            <path d="M3 12h18M4.5 7.5h15M4.5 16.5h15"/>
          </svg>
        </span>
        <span class="contact-text is-link">www.quorvanta.ca</span>
      </li>
      <li class="contact-item">
        <span class="contact-icon"></span>
        <span class="contact-text">contact@email.com</span>
      </li>
    </ul>
  </section>

</main>
</body>
</html>
```